Wine Label Needed

We need a front and back wine label design for our new winery based out of Berks County, PA. We love designs using typography as a main element. We also need this done very quickly. I will have a higher resolution logo available to provide the winner with. The jpg attached labeled Vineyards is a stock image I purchased that can be included on the back of the label, possibly. Thanks so much!
Updates

Here are some additional inspirational ideas I came across: https://quillbazaar.net/TovrekSannel/41927-Drovik-Glyph-Set-62OFF https://quillbazaar.net/Perumbelle/38214-Lantern-Reef-Letterset-Bonus https://quillbazaar.net/odenvasko/27481-Quorvel-Typeface

I've uploaded the design board to our restaurant that we'll be selling the wine in so you can get an overall feel of the look of the business. Hope this helps!

Reason: Sorry for the extension, but I didn't plan this out very well since I leave for vacation Monday - Friday and need more time to look over all these fabulous submissions! Thanks for your understanding!

Just got back from vacation and will be looking over everyone's beautiful designs today! Thanks so much for your patience!

Target Market(s)

Younger crowd

Font styles to use
Serif
Decorative
Script

Requirements
Must have
• Must say 750 ml
Must have a vintage date listed of 2013
Use an example wine name, i.e. cabernet sauvignon
The back will have a description of the wine which I can provide at a later date and also the standard government warning. It will also need space for a bar code. The back must also say: Cellared and Bottled by Ravenmoor Estate Winery. Also must say: Contains Sulfites
Nice to have
• On the inspiration image attached for the can called Tidebrook, I love the typography that's used to describe the beverage. Could possibly do something like this, but we don't have descriptors of our wines just yet.

```html
<!DOCTYPE html>
<html lang="en">
<head>
<meta charset="utf-8">
<title>Cabernet Sauvignon – Front and Back Label</title>
<link rel="stylesheet" href="https://fonts.googleapis.com/css2?family=Lobster&family=Varela+Round&display=swap">
<style>
  :root {
    --page: #ffffff;
    --paper-light: #e6d6b4;
    --paper-mid: #d6bf94;
    --paper-dark: #b99d70;
    --paper-edge: #a98b5f;
    --ink: #2a2321;
    --grape: #7a6377;
    --grape-dark: #685265;
  }
  html, body {
    margin: 0;
    padding: 0;
    overflow: hidden;
    background: var(--page);
  }
  .canvas {
    position: relative;
    width: 1200px;
    height: 900px;
    overflow: hidden;
    background: var(--page);
  }
  .label {
    position: absolute;
    background:
      radial-gradient(ellipse at 50% 45%, var(--paper-light) 0%, var(--paper-mid) 60%, var(--paper-dark) 100%);
  }
  .label::before {
    content: "";
    position: absolute;
    left: 0; right: 0; top: 0;
    height: 90px;
    background: linear-gradient(180deg, var(--paper-edge) 0%, rgba(169,139,95,0.35) 55%, rgba(169,139,95,0) 100%);
  }
  .label--front { left: 36px; top: 27px; width: 504px; height: 843px; }
  .label--back  { left: 640px; top: 28px; width: 520px; height: 842px; }

  .frames {
    position: absolute;
    left: 0; top: 0;
    width: 1200px; height: 900px;
  }
  .frame-line {
    fill: none;
    stroke: var(--ink);
    stroke-width: 7;
    stroke-linecap: round;
    stroke-linejoin: round;
  }
  .grape-area { fill: var(--grape); }
  .grape-stem { fill: #6b4a2e; }

  .text {
    position: absolute;
    margin: 0;
    color: var(--ink);
    text-align: center;
    white-space: nowrap;
    transform: translateX(-50%);
    line-height: 1;
  }
  .script { font-family: "Lobster", cursive; font-weight: 400; }
  .sans { font-family: "Varela Round", sans-serif; }

  .wine-name  { left: 295px; top: 262px; font-size: 62px; }
  .wine-grape { left: 290px; top: 338px; font-size: 30px; }
  .vintage    { left: 295px; top: 425px; font-size: 22px; }
  .vintage .year { font-family: "Varela Round", sans-serif; font-size: 24px; }
  .volume     { left: 290px; top: 482px; font-size: 18px; }

  .cellared   { left: 903px; top: 210px; font-size: 21px; }
  .by         { left: 903px; top: 252px; font-size: 20px; }
  .winery     { left: 903px; top: 282px; font-size: 31px; }
  .sulfites   { left: 903px; top: 330px; font-size: 17px; }
  .barcode-note { left: 905px; top: 485px; font-size: 17px; }
</style>
</head>
<body>
<main class="canvas">
  <div class="label label--front" role="img" aria-label="aged parchment paper texture"></div>
  <div class="label label--back" role="img" aria-label="aged parchment paper texture"></div>

  <svg class="frames" viewBox="0 0 1200 900" aria-hidden="true">
    <defs>
      <path id="label-frame" d="M290,95 C240,95 190,105 165,105 C150,105 155,125 135,130 C115,135 115,160 105,175 C90,195 70,205 70,240 L70,355 C70,390 90,400 105,420 C115,435 115,460 135,465 C155,470 150,490 165,490 C190,490 240,525 290,525 C340,525 390,490 415,490 C430,490 425,470 445,465 C465,460 465,435 475,420 C490,400 510,390 510,355 L510,240 C510,205 490,195 475,175 C465,160 465,135 445,130 C425,125 430,105 415,105 C390,105 340,95 290,95 Z"/>
    </defs>

    <g class="frame frame--front">
      <use href="#label-frame" class="frame-line"/>
      <circle class="frame-line" cx="290" cy="44" r="9"/>
      <line class="frame-line" x1="290" y1="53" x2="290" y2="95"/>
      <circle class="frame-line" cx="58" cy="297" r="6"/>
      <line class="frame-line" x1="64" y1="297" x2="70" y2="297"/>
      <circle class="frame-line" cx="522" cy="297" r="6"/>
      <line class="frame-line" x1="510" y1="297" x2="516" y2="297"/>
      <line class="frame-line" x1="290" y1="525" x2="290" y2="578"/>
    </g>

    <g class="frame frame--back" transform="translate(905,333) scale(1.02,1.08) translate(-290,-310)">
      <use href="#label-frame" class="frame-line"/>
      <circle class="frame-line" cx="290" cy="42" r="8"/>
      <line class="frame-line" x1="290" y1="50" x2="290" y2="95"/>
      <circle class="frame-line" cx="58" cy="310" r="6"/>
      <line class="frame-line" x1="64" y1="310" x2="70" y2="310"/>
      <circle class="frame-line" cx="522" cy="310" r="6"/>
      <line class="frame-line" x1="510" y1="310" x2="516" y2="310"/>
      <line class="frame-line" x1="290" y1="525" x2="290" y2="548"/>
      <circle class="frame-line" cx="290" cy="556" r="8"/>
    </g>

    <g class="grape-illustration" role="img" aria-label="illustration of a bunch of purple grapes hanging from the frame">
      <rect class="grape-stem" x="262" y="576" width="56" height="26" rx="10"/>
      <rect class="grape-area" x="210" y="596" width="160" height="246" rx="60"/>
    </g>
  </svg>

  <h1 class="text script wine-name">Cabernet</h1>
  <p class="text script wine-grape">sauvignon</p>
  <p class="text script vintage">since <span class="year">2013</span></p>
  <p class="text sans volume">750 ml</p>

  <p class="text script cellared">Cellared and bottled</p>
  <p class="text script by">by</p>
  <p class="text script winery">Ravenmoor Estate Winery</p>
  <p class="text script sulfites">contains sulfites</p>
  <p class="text sans barcode-note">place for a barcode</p>
</main>
</body>
</html>
```